Card Design to Advertise New Business

I am looking to have a card designed so that I can pass it out to help promote my business. I have never done this before so I honestly do not know where to start with any ideas. I am providing my website address to help. I provide math tutoring, test prep, and schooling options.

I am looking for a card bigger than a business card but smaller than a flyer. Something front and back that I can pass out.

Business Information
Phone: 470-526-1984
Website: www.brightmaplestudyhub.com
Address: 418 Larkwood Rd Ste 210 Marietta GA 30068
Email: brightmapleservices@kestrelpostmail.com

Services:
Math Tutoring
SAT & ACT Test Prep
Group and Private Sessions
Fully Accredited Private School

Target Market(s)

Middle and High School Students

Industry/Entity Type

Education

Requirements
Must have
• Information from my website

```html
<!DOCTYPE html>
<html lang="en">
<head>
<meta charset="utf-8">
<title>Bright Maple Study Hub – Flyer</title>
<link href="https://fonts.googleapis.com/css2?family=Roboto:wght@400;500;700;900&display=swap" rel="stylesheet">
<style>
  :root {
    --page-bg: #a9a9a9;
    --paper: #ffffff;
    --brand-blue: #3766c9;
    --brand-green: #3cc43e;
    --lavender: #ccd6f2;
    --service-red: #d22d0c;
    --mission-green: #21c21b;
    --ink: #1c1c1c;
    --divider: #5aa9d3;
    --group-box: #54a9d6;
    --group-box-back: #cfe6f3;
    --private-box: #c8c21a;
    --private-box-back: #ecebc5;
    --contact-blue: #2f56c4;
  }
  * { margin: 0; padding: 0; box-sizing: border-box; }
  html, body { width: 1052px; height: 1200px; overflow: hidden; }
  body { background: var(--page-bg); font-family: "Roboto", Arial, sans-serif; }

  .flyer {
    position: absolute; left: 126px; top: 0;
    width: 800px; height: 1200px;
    background: var(--paper); overflow: hidden;
  }
  .hero-art { position: absolute; inset: 0; }

  .tagline {
    position: absolute; left: 21px; top: 452px;
    color: #fff; font-weight: 700; font-size: 24px; letter-spacing: -0.2px;
    white-space: nowrap;
  }
  .headline {
    position: absolute; left: 8px; top: 484px; width: 440px;
    color: #fff; font-weight: 900; font-size: 60px; line-height: 64px;
    text-align: center; letter-spacing: -0.5px; white-space: nowrap;
  }

  .brand-name {
    position: absolute; left: 520px; top: 650px; width: 265px;
    text-align: center; color: var(--brand-blue);
    font-weight: 700; font-size: 30px; line-height: 32px;
  }

  .services, .mission { position: absolute; top: 763px; }
  .services { left: 28px; width: 380px; }
  .mission { left: 457px; width: 330px; }
  .section-title { font-weight: 700; font-size: 46px; line-height: 54px; white-space: nowrap; }
  .services .section-title { color: var(--service-red); }
  .mission .section-title { color: var(--mission-green); }

  .service-list { list-style: none; }
  .service-list li {
    position: relative; padding-left: 24px;
    font-size: 25px; line-height: 32.5px; color: var(--ink);
  }
  .service-list li::before {
    content: ""; position: absolute; left: 2px; top: 11px;
    width: 13px; height: 13px; border-radius: 50%; background: var(--service-red);
  }
  .mission-text {
    padding-left: 6px; font-size: 23px; line-height: 30.2px; color: var(--ink);
    white-space: nowrap;
  }

  .divider {
    position: absolute; left: 424px; top: 767px;
    width: 2px; height: 223px; background: var(--divider);
  }

  .price-layer { position: absolute; inset: 0; z-index: 0; isolation: isolate; }
  .price-box {
    position: absolute; top: 1015px; width: 353px; height: 71px;
    color: #fff; font-weight: 700; font-size: 21.5px; line-height: 27px;
    display: flex; align-items: center; justify-content: center; text-align: center;
  }
  .price-box::before {
    content: ""; position: absolute; left: -9px; top: -9px;
    width: 351px; height: 71px; z-index: -1;
  }
  .price-box.group { left: 34px; background: var(--group-box); }
  .price-box.group::before { background: var(--group-box-back); }
  .price-box.private { left: 411px; background: var(--private-box); }
  .price-box.private::before { background: var(--private-box-back); }

  .contact-shadow {
    position: absolute; left: 28px; top: 1125px; width: 730px; height: 71px;
    border-radius: 36px; background: var(--lavender);
  }
  .contact-bar {
    position: absolute; left: 34px; top: 1117px; width: 732px; height: 70px;
    border: 3px solid var(--contact-blue); border-radius: 36px;
    background: linear-gradient(#ffffff, #f1f3fb);
  }
  .phone {
    position: absolute; left: 62px; top: 1128px;
    display: flex; align-items: center; gap: 5px;
    color: var(--service-red); font-weight: 700; font-size: 26px; white-space: nowrap;
  }
  .website {
    position: absolute; left: 66px; top: 1161px;
    display: flex; align-items: center; gap: 7px;
    color: var(--contact-blue); font-size: 11px; white-space: nowrap;
  }
  .contact-heading {
    position: absolute; left: 340px; top: 1123px;
    color: var(--contact-blue); font-weight: 700; font-size: 17px; white-space: nowrap;
  }
  .address, .email {
    position: absolute; left: 500px;
    display: flex; gap: 7px; color: var(--contact-blue);
    font-size: 11.5px; font-weight: 500; white-space: nowrap;
  }
  .address { top: 1124px; line-height: 16px; align-items: flex-start; }
  .email { top: 1162px; align-items: center; letter-spacing: -0.1px; }
  .icon { flex: none; }
</style>
</head>
<body>
<main class="flyer">
  <svg class="hero-art" width="800" height="1200" viewBox="0 0 800 1200">
    <defs>
      <linearGradient id="photoTone" x1="0" y1="0" x2="1" y2="0.3">
        <stop offset="0" stop-color="#3d5a3a"/>
        <stop offset="0.55" stop-color="#4a6b45"/>
        <stop offset="0.8" stop-color="#b58a3a"/>
        <stop offset="1" stop-color="#e9b632"/>
      </linearGradient>
      <linearGradient id="waveTone" x1="0" y1="0" x2="1" y2="0">
        <stop offset="0" stop-color="#3766c9"/>
        <stop offset="0.45" stop-color="#3a6bc4"/>
        <stop offset="0.75" stop-color="#3ea27a"/>
        <stop offset="1" stop-color="#3cc43e"/>
      </linearGradient>
    </defs>
    <rect x="0" y="0" width="800" height="520" fill="url(#photoTone)" role="img" aria-label="Photo: a student writing equations on a green chalkboard while a tutor in a yellow top looks on"/>
    <path d="M0,694 C250,690 430,600 560,520 C640,480 720,470 800,520 L800,1200 L0,1200 Z" fill="#ffffff"/>
    <path d="M0,320 C200,520 470,470 560,520 C470,600 280,700 0,716 Z" fill="var(--lavender)"/>
    <path d="M0,298 C110,370 300,438 520,446 C660,450 740,455 800,504 L800,520 C720,480 640,480 560,520 C430,600 250,690 0,694 Z" fill="url(#waveTone)"/>
  </svg>

  <p class="tagline">MORE THAN JUST MATH TUTORING;</p>
  <h1 class="headline">WE ARE MAPLE<br>COACHES</h1>

  <p class="brand-name">BRIGHT MAPLE<br>STUDY HUB</p>

  <section class="services">
    <h2 class="section-title">SERVICES:</h2>
    <ul class="service-list">
      <li>Math Tutoring</li>
      <li>SAT &amp; ACT Test Prep</li>
      <li>Group and Private Sessions</li>
      <li>Fully Accredited<br>Private School</li>
    </ul>
  </section>

  <div class="divider"></div>

  <section class="mission">
    <h2 class="section-title">OUR MISSION:</h2>
    <p class="mission-text">To use optimistic mindsets<br>to teach others to be<br>confident in taking risks<br>despite life's current and<br>possible challenges.</p>
  </section>

  <div class="price-layer">
    <div class="price-box group">GROUP SESSIONS STARTING<br>AS LOW AS $30 AN HOUR</div>
    <div class="price-box private">PRIVATE SESSIONS STARTING<br>AT $60 AN HOUR</div>
  </div>

  <div class="contact-shadow"></div>
  <div class="contact-bar"></div>

  <div class="phone">
    <svg class="icon" width="22" height="22" viewBox="0 0 24 24"><path d="M6.6 10.8a15 15 0 0 0 6.6 6.6l2.2-2.2c.3-.3.7-.4 1-.2 1.1.4 2.3.6 3.6.6.6 0 1 .4 1 1V20c0 .6-.4 1-1 1A17 17 0 0 1 3 4c0-.6.4-1 1-1h3.5c.6 0 1 .4 1 1 0 1.3.2 2.5.6 3.6.1.3 0 .7-.2 1z" fill="var(--service-red)"/><path d="M14 3a7 7 0 0 1 7 7M14 6.5a3.5 3.5 0 0 1 3.5 3.5" stroke="var(--service-red)" stroke-width="2" fill="none"/></svg>
    <span>470-526-1984</span>
  </div>
  <div class="website">
    <svg class="icon" width="13" height="13" viewBox="0 0 24 24" fill="none" stroke="var(--contact-blue)" stroke-width="2"><circle cx="12" cy="12" r="10"/><path d="M2 12h20M12 2c3 3 3 17 0 20M12 2c-3 3-3 17 0 20"/></svg>
    <span>www.brightmaplestudyhub.com</span>
  </div>

  <p class="contact-heading">CONTACT US</p>

  <div class="address">
    <svg class="icon" width="13" height="18" viewBox="0 0 24 32"><path d="M12 1a10 10 0 0 0-10 10c0 7 10 17 10 17s10-10 10-17A10 10 0 0 0 12 1z" fill="none" stroke="var(--contact-blue)" stroke-width="3"/><circle cx="12" cy="11" r="3.5" fill="var(--contact-blue)"/><rect x="4" y="29" width="16" height="2.5" fill="var(--contact-blue)"/></svg>
    <span>418 Larkwood Rd Ste<br>210 Marietta GA 30068</span>
  </div>
  <div class="email">
    <svg class="icon" width="19" height="13" viewBox="0 0 28 18"><rect x="1" y="1" width="26" height="16" fill="none" stroke="var(--contact-blue)" stroke-width="2"/><path d="M1 1l13 10L27 1M1 17l10-8M27 17l-10-8" fill="none" stroke="var(--contact-blue)" stroke-width="2"/></svg>
    <span>brightmapleservices@kestrelpostmail.com</span>
  </div>
</main>
</body>
</html>
```